Web site for new fundraising service for charities

We need a web design for a new charitable trust based in New Zealand. With the economic downturn, charities are finding it increasingly difficult to raise the monies they need to deliver their services.

Using a network of fundraisers working out of their homes, KindLoop (our charitable trust) will source unique, high interest auction items on behalf of multiple charities - things like luxury cruises, exotic travel, luxury accommodation, fine dining, unique experiences with sports and entertainment personalities, tickets to sporting and entertainment events, etc.

Once we have sourced sufficient high value items we will then partner with SellNest (NZ's equivalent of bidRo) to launch the auction. The proceeds from each auction will benefit up to 6 charities. The auctions will be promoted through SellNest, through PR, and through the communications channels of the benefiting charities, reaching a wider audience than would be possible if just one charity was holding an auction and therefore resulting in more competitive bidding and higher returns for the charities.

We need a web site that we can point potential donors of auction items to, that gives them confidence in KindLoop. We will also leverage the web site with journalists. And of course, charities who are wondering whether or not to use KindLoop will come to our web site and check out our credentials. The tone of the site needs to be warm, friendly, approachable.

We are not locked into the blue and orange colors of the logo and in fact are experimenting with other colors as we speak.

Please note that what we're looking for is the design for the home page, plus a sub page design.

Target Market(s)

CEOs, corporate social responsibility managers, general managers, business owners, charities, the media

Industry/Entity Type

Communications

Requirements
Must have
• Video on home page
Newsletter sign up on all pages
Navigation as per the attached PDF example

```html
<!DOCTYPE html>
<html lang="en">
<head>
<meta charset="utf-8">
<title>KindLoop – Home</title>
<link rel="stylesheet" href="https://fonts.googleapis.com/css2?family=Lato:ital,wght@0,400;0,700;1,700&display=swap">
<style>
:root{
  --bg-dark:#2e2e2e;
  --bg-mid:#4a4a4a;
  --text-light:#f2f2f2;
  --text-muted:#d8d8d8;
  --brand-blue:#5b8fe0;
  --brand-gold:#d9a03a;
  --navy:#0f2350;
  --panel-orange:#d88b1c;
  --submit-blue:#0b7fc0;
  --quote-gold:#f0b41c;
  --menu-bg:#f2f4f6;
  --menu-text:#2a2a2a;
}
*{box-sizing:border-box;margin:0;padding:0}
html,body{width:1200px;height:707px;overflow:hidden}
body{
  font-family:"Lato",sans-serif;
  background:radial-gradient(ellipse at 50% 45%,var(--bg-mid) 0%,#3a3a3a 55%,var(--bg-dark) 100%);
  color:var(--text-light);
  position:relative;
}
.backdrop{position:absolute;left:0;top:380px;width:1200px;height:230px;
  background:linear-gradient(180deg,rgba(255,255,255,0.02),rgba(255,255,255,0.06),rgba(255,255,255,0.02))}
.abs{position:absolute}

.logo{left:203px;top:36px;display:flex;align-items:center;gap:10px}
.logo-dot{width:44px;height:44px;border-radius:50%;background:var(--brand-gold)}
.logo-name{font-size:28px;font-weight:700;color:var(--brand-blue)}

.main-nav{left:485px;top:54px;display:flex;font-size:17px;letter-spacing:.3px}
.main-nav a{color:var(--text-light);text-decoration:none;padding:0 19px;border-left:1px dotted #777}
.main-nav a:first-child{padding-left:0;border-left:none}

.social{display:flex;gap:14px;font-size:12px;font-weight:700;color:var(--text-light)}
.social.top{left:850px;top:58px}
.social.bottom{left:840px;top:621px;color:#aaa}

.header-rule{left:200px;top:96px;width:800px;height:1px;background:linear-gradient(90deg,transparent,#1f1f1f 15%,#1f1f1f 85%,transparent)}

.side-menu{left:211px;top:147px;width:176px;height:219px;background:linear-gradient(180deg,#fff,var(--menu-bg) 60%,#dde2e7);
  box-shadow:0 4px 8px rgba(0,0,0,.5);border-radius:3px 0 0 3px;list-style:none;padding-top:6px}
.side-menu li{height:35.5px;margin:0 22px 0 24px;border-bottom:1px dotted #bbb;text-align:right;font-size:13px;line-height:35px;color:var(--menu-text)}
.side-menu li:last-child{border-bottom:none}
.side-menu li.active{margin:0 0 6px -5px;padding-right:22px;height:26px;line-height:26px;background:var(--navy);color:#fff;border-bottom:none;
  clip-path:polygon(0 0,100% 0,100% 100%,0 100%,5px 50%)}

.video-frame{left:385px;top:122px;width:415px;height:260px;background:#fafafa;box-shadow:0 3px 8px rgba(0,0,0,.5);padding:7px}
.video-still{width:100%;height:100%;background:linear-gradient(180deg,#3c3c3c 0%,#6a6a6a 45%,#2a2a2a 70%,#1b1b1b 100%);position:relative}
.play{position:absolute;left:148px;top:65px;width:92px;height:92px}

.subscribe{left:800px;top:147px;width:193px;height:220px;background:linear-gradient(180deg,#e39a27,var(--panel-orange));border-radius:0 3px 3px 0;
  box-shadow:0 4px 8px rgba(0,0,0,.5);padding:9px 11px}
.subscribe h2{font-weight:400;font-size:24px;line-height:28px;color:#fff}
.subscribe p{font-size:9.6px;line-height:12.4px;color:#fff;margin-top:5px;height:67px}
.field{background:#fff;height:19px;font-size:9.5px;color:#aaa;padding:3px 6px;margin-top:5px}
.row{display:flex;gap:5px;margin-top:8px}
.row .field{margin-top:0;flex:1}
.submit{margin-top:5px;height:25px;background:linear-gradient(180deg,#1a98d6,var(--submit-blue));border:1px solid #0a4f7a;color:#fff;font-weight:700;font-size:19px;text-align:center;line-height:23px}

.quote-mark{z-index:0;left:222px;top:372px;font-size:150px;font-weight:700;color:#888;opacity:.45;line-height:1}
.quote-mark.close{left:830px;top:502px;font-size:90px;opacity:.35}
.quote{z-index:1;left:268px;top:428px;font-size:21px;line-height:25px;color:var(--text-light);white-space:nowrap}
.author{z-index:1;left:268px;top:537px;font-size:21px;font-weight:700;font-style:italic;color:var(--quote-gold)}

.dotted{left:198px;width:802px;height:0;border-top:1px dotted #111}
.foot-mark{left:202px;top:615px;width:26px;height:26px;border-radius:50%;background:#aaa}
.foot-nav{left:346px;top:621px;display:flex;gap:15px;font-size:10.6px;color:var(--text-light)}
.copyright{left:0;top:666px;width:1200px;text-align:center;font-size:10.4px;color:var(--text-muted)}
</style>
</head>
<body>
<div class="backdrop abs" role="img" aria-label="Faded collage of travel and event photographs"></div>

<div class="logo abs"><span class="logo-dot"></span><span class="logo-name">KindLoop</span></div>

<nav class="main-nav abs"><a>DONOR</a><a>CHARITIES</a><a>AUCTIONS</a></nav>
<div class="social top abs"><span>Friendly</span><span>Chirp</span><span>Linkwork</span><span>Feed</span></div>
<div class="header-rule abs"></div>

<ul class="side-menu abs">
  <li class="active">Home</li>
  <li>How it Works</li>
  <li>Acts of Goodness</li>
  <li>Goodness Partners</li>
  <li>About</li>
  <li>Contact</li>
</ul>

<div class="video-frame abs">
  <div class="video-still" role="img" aria-label="Video still of an overwater bungalow on a calm sea">
    <svg class="play" viewBox="0 0 92 92">
      <circle cx="46" cy="46" r="46" fill="#555"/>
      <circle cx="46" cy="46" r="39" fill="#e6e6e6"/>
      <path d="M37 32 L60 46 L37 60 Z" fill="#111"/>
    </svg>
  </div>
</div>

<form class="subscribe abs">
  <h2>Subscribe</h2>
  <p>Charity auctions are a great way to get luxury items and unique experiences while helping a worthwhile cause. Subscribe to our email list to be kept informed about upcoming auctions.</p>
  <div class="row"><div class="field">First Name</div><div class="field">Last Name</div></div>
  <div class="field">City / Town</div>
  <div class="field">Email Address</div>
  <div class="submit">Submit</div>
</form>

<div class="quote-mark abs">“</div>
<div class="quote-mark close abs">”</div>
<blockquote class="quote abs">In the end, though, maybe we must all give up trying to pay back the people<br>in this world who sustain our lives. In the end, maybe it’s wiser to surrender<br>before the miraculous scope of human generosity and to just keep saying<br>thank you, forever and sincerely, for as long as we have voices.</blockquote>
<div class="author abs">— Maren Holloway</div>

<div class="dotted abs" style="top:598px"></div>
<div class="foot-mark abs"></div>
<nav class="foot-nav abs"><span>Home</span><span>How it Works</span><span>Acts of Goodness</span><span>Goodness Partners</span><span>About</span><span>Contact</span></nav>
<div class="social bottom abs"><span>Friendly</span><span>Chirp</span><span>Linkwork</span><span>Feed</span></div>
<div class="dotted abs" style="top:655px"></div>
<div class="copyright abs">Copyrights © KindLoop. All rights reserved.</div>
</body>
</html>
```